Business cards real estate company

We need a design for a business card. It is a company that specializes in real estate sales. There should be space for a photo of the respective employee as well as the website and telephone number on it. Design should be noble, innovative.

Contact Information for Business Card

Website, Name, Position, Telefonnummer

Requirements
Must have
• Photo, logo

```html
<!DOCTYPE html>
<html lang="en">
<head>
<meta charset="utf-8">
<title>Verdanest – Business Card</title>
<link rel="stylesheet" href="https://fonts.googleapis.com/css2?family=Montserrat:wght@400;500;600;700&display=swap">
<style>
  :root {
    --page-bg: #e9ebe6;
    --card-white: #ffffff;
    --green-deep: #5aa83a;
    --green-mid: #79bb45;
    --green-lime: #bcd633;
    --green-pale: #eef5de;
    --green-soft: #dbeac6;
    --text-dark: #2b2b2b;
    --card-shadow: 0 14px 30px rgba(0, 0, 0, 0.18);
  }
  * { box-sizing: border-box; margin: 0; padding: 0; }
  html, body {
    width: 1200px;
    height: 900px;
    overflow: hidden;
    background: var(--page-bg);
    font-family: "Montserrat", sans-serif;
  }
  .sheet {
    width: 1200px;
    height: 900px;
    display: flex;
    flex-direction: column;
    align-items: center;
    justify-content: center;
    gap: 44px;
  }
  .card {
    width: 680px;
    height: 388px;
    border-radius: 30px;
    position: relative;
    overflow: hidden;
    box-shadow: var(--card-shadow);
  }

  /* Front */
  .card-front { background: var(--card-white); }
  .accent-square {
    position: absolute;
    left: 0;
    top: 82px;
    width: 24px;
    height: 24px;
    background: var(--green-lime);
  }
  .contact-block {
    position: absolute;
    left: 46px;
    top: 78px;
    color: var(--text-dark);
  }
  .person-name {
    font-weight: 600;
    font-size: 25px;
    line-height: 1.2;
    letter-spacing: 1px;
    color: var(--green-mid);
    text-transform: uppercase;
  }
  .person-role {
    display: flex;
    align-items: center;
    gap: 6px;
    font-size: 17px;
    margin-top: 2px;
  }
  .role-rule {
    width: 530px;
    height: 1.5px;
    background: var(--green-mid);
  }
  .address {
    font-size: 17px;
    line-height: 1.35;
    margin-top: 14px;
  }
  .contact-list {
    list-style: none;
    margin-top: 8px;
    font-size: 17px;
    line-height: 1.4;
  }
  .contact-list li {
    display: flex;
    align-items: center;
    gap: 8px;
  }
  .contact-icon {
    width: 12px;
    height: 12px;
    flex: none;
  }
  .brand-front {
    position: absolute;
    right: 48px;
    top: 54px;
    font-weight: 600;
    font-size: 46px;
    line-height: 1;
    color: var(--green-mid);
    letter-spacing: 0.5px;
  }
  .employee-photo {
    position: absolute;
    right: 48px;
    top: 178px;
    width: 150px;
    height: 170px;
    border-radius: 14px;
    background: linear-gradient(160deg, var(--green-pale), var(--green-soft));
    border: 2px solid var(--green-mid);
  }

  /* Back */
  .card-back {
    background: linear-gradient(118deg, var(--green-mid) 0 50%, var(--green-lime) 50% 100%);
    display: flex;
    align-items: center;
    justify-content: center;
  }
  .brand-back {
    font-weight: 700;
    font-size: 92px;
    color: var(--green-deep);
    letter-spacing: 1px;
  }
</style>
</head>
<body>
<main class="sheet">
  <section class="card card-front" aria-label="Business card front">
    <span class="accent-square"></span>
    <p class="brand-front">Verdanest</p>
    <div class="contact-block">
      <h1 class="person-name">Daniel Hart</h1>
      <p class="person-role">Owner <span class="role-rule"></span></p>
      <p class="address">48 Alder Lane<br>Maple Grove, IL 60512</p>
      <ul class="contact-list">
        <li>
          <svg class="contact-icon" viewBox="0 0 12 12"><path d="M3 1 L5 3.5 L4 5 Q5.5 7.5 7 8 L8.5 7 L11 9 L9.5 11 Q4 10.5 1 2.5 Z" fill="var(--green-mid)"/></svg>
          555-014-2290
        </li>
        <li>
          <svg class="contact-icon" viewBox="0 0 12 12"><rect x="1" y="2.5" width="10" height="7" fill="none" stroke="var(--green-mid)" stroke-width="1.2"/><path d="M1 2.5 L6 6.5 L11 2.5" fill="none" stroke="var(--green-mid)" stroke-width="1.2"/></svg>
          hello@verdanest.com
        </li>
        <li>
          <svg class="contact-icon" viewBox="0 0 12 12"><circle cx="6" cy="6" r="5" fill="none" stroke="var(--green-mid)" stroke-width="1.2"/><path d="M1 6 H11 M6 1 V11 M6 1 Q2.5 6 6 11 M6 1 Q9.5 6 6 11" fill="none" stroke="var(--green-mid)" stroke-width="0.9"/></svg>
          www.verdanest.com
        </li>
      </ul>
    </div>
    <div class="employee-photo" role="img" aria-label="Portrait photo of the employee"></div>
  </section>

  <section class="card card-back" aria-label="Business card back">
    <p class="brand-back">Verdanest</p>
  </section>
</main>
</body>
</html>
```